Bright Path Academy - Personal Development business 2.0 needs a social post format design.

https://www.brightpathacademy-example.com

Our focus with Bright Path Academy is on developing people through knowledge and skills to improve their everyday lives.
We love simplicity, Quince design and less is more.

We are crazy about personal growth, science, design, the latest gadgets and people.

We need 4 formats for our social media posts.
1. Blogs -to pronounce a blog post
2. Workshop /training - to pronounce our workshops/trainings (both online and offline)
3. Podcast - called "Kijk eens verder". To pronounce a guest we've spoken. The host is called Berend.
4. Facts - to pronounce short facts about personal development. Invites people to read more.
The formats should include: high quality pictogram (better than the uploaded picto's), 1 of the 3 logo's in the design.
It's important that we can edit the design in Lumora Draw / Lumora Pixel to adjust the text in the format.

Attached you find four of our current designs, which are a poor example of how the designs should look like. These are just to show you how much lines of text (more or less) will be in the designs. So please do not make a design that looks like these ;) You have carte blanche.

Our customers are mostly women (80%). We focus on both business and casual customers.

Target Market(s)

80% woman, 20% men. We focus on both business and casual customers.

Requirements
Must have
• Less is more. Quince Design alike. Simplicity.
Aimed at the women target audience.
Designs must be edible for adjusting the text in the format.
Nice to have
• Unique concept.
The design should "breathe".
Each design can have a different color, so customers identify the specific post with specific information. For example, blog is red, workshop post black, etc.

```html
<!DOCTYPE html>
<html lang="nl">
<head>
<meta charset="utf-8">
<title>Bright Path Academy – social post formats</title>
<link rel="stylesheet" href="https://fonts.googleapis.com/css2?family=Montserrat:wght@400;600;700;800&display=swap">
<style>
  :root{
    --canvas:#5a5a5a;
    --white:#ffffff;
    --ink:#1d1d1d;
    --blog:#f39506;
    --blog-ring:#f9a11c;
    --train:#000000;
    --train-ring:#2c2c2c;
    --pod:#4f94d4;
    --pod-ring:#60a6e3;
    --fact:#278006;
    --fact-ring:#2d9f0b;
    --photo-light:#d9dde2;
    --photo-mid:#9aa0a8;
    --photo-dark:#3a3d44;
  }
  *{margin:0;padding:0;box-sizing:border-box}
  html,body{width:1200px;height:857px;overflow:hidden;background:var(--canvas)}
  body{position:relative;font-family:"Montserrat",sans-serif}
  .post{position:absolute;width:349px;height:349px;background:var(--white);overflow:hidden}
  .post--blog{left:223px;top:74px;--accent:var(--blog);--ring:var(--blog-ring)}
  .post--training{left:628px;top:64px;--accent:var(--train);--ring:var(--train-ring)}
  .post--podcast{left:233px;top:444px;--accent:var(--pod);--ring:var(--pod-ring)}
  .post--facts{left:628px;top:444px;--accent:var(--fact);--ring:var(--fact-ring)}
  .post__art{position:absolute;inset:0}
  .band{fill:var(--accent)}
  .ring{fill:var(--ring)}
  .badge{position:absolute;left:0;top:7px;height:37px;padding:0 22px 0 10px;display:flex;align-items:center;gap:5px;
    background:var(--accent);color:var(--white);border-radius:0 19px 19px 0;font-weight:700;font-size:11px;letter-spacing:.2px}
  .post--training .badge{top:9px;height:31px;font-size:9.5px;font-weight:600}
  .badge svg{width:19px;height:19px;flex:none}
  .caption{position:absolute;left:40px;right:40px;color:var(--white);text-align:center;line-height:1.25}
  .caption--blog{top:206px;font-weight:800;font-size:15.5px}
  .caption--training{top:194px}
  .caption__title{display:block;font-weight:800;font-size:19px;line-height:1.1}
  .caption__sub{display:block;font-weight:400;font-size:11.5px;margin-top:3px;letter-spacing:.3px}
  .caption--podcast{top:195px}
  .caption__lead{display:block;font-weight:400;font-size:16px;letter-spacing:.4px}
  .caption__name{display:block;font-weight:800;font-size:21px;line-height:1.05}
  .caption--facts{top:206px;font-weight:800;font-size:12.5px;left:55px;right:55px}
  .brand{position:absolute;right:11px;bottom:8px;text-align:center;color:var(--ink);font-weight:600;line-height:1}
  .brand__name{display:block;font-size:13px}
  .brand__tag{display:block;font-size:4px;letter-spacing:2px;margin-top:2px}
</style>
</head>
<body>
<svg width="0" height="0" style="position:absolute" aria-hidden="true">
  <defs>
    <radialGradient id="photoTone" cx="50%" cy="35%" r="70%">
      <stop offset="0" stop-color="#e4e7ea"/>
      <stop offset=".55" stop-color="#a7adb5"/>
      <stop offset="1" stop-color="#4a4e56"/>
    </radialGradient>
    <linearGradient id="photoShade" x1="0" y1="0" x2="0" y2="1">
      <stop offset=".35" stop-color="#1f2228" stop-opacity="0"/>
      <stop offset="1" stop-color="#1f2228" stop-opacity=".75"/>
    </linearGradient>
  </defs>
</svg>

<!-- Blog -->
<section class="post post--blog">
  <svg class="post__art" viewBox="0 0 349 349">
    <polygon class="band" points="234,0 349,0 349,115 115,349 0,349 0,234"/>
    <circle class="ring" cx="175" cy="174" r="139"/>
    <g role="img" aria-label="Foto: vrouw met bril en tablet in een licht kantoor">
      <circle cx="175" cy="174" r="128" fill="url(#photoTone)"/>
      <circle cx="175" cy="174" r="128" fill="url(#photoShade)"/>
    </g>
  </svg>
  <div class="badge">
    <svg viewBox="0 0 24 24" fill="none" stroke="currentColor" stroke-width="2" stroke-linecap="round" stroke-linejoin="round"><path d="M4 20h4L19 9l-4-4L4 16z"/><path d="M13 7l4 4"/></svg>
    BLOG
  </div>
  <p class="caption caption--blog">Goede voornemens<br>die je volhoudt - 3 tips</p>
  <div class="brand"><span class="brand__name">Bright Path</span><span class="brand__tag">ACADEMY</span></div>
</section>

<!-- Online training -->
<section class="post post--training">
  <svg class="post__art" viewBox="0 0 349 349">
    <polygon class="band" points="234,0 349,0 349,115 115,349 0,349 0,234"/>
    <circle class="ring" cx="175" cy="174" r="139"/>
    <g role="img" aria-label="Foto: glimlachende man met gekruiste armen in een kantoor">
      <circle cx="175" cy="174" r="128" fill="url(#photoTone)"/>
      <circle cx="175" cy="174" r="128" fill="url(#photoShade)"/>
    </g>
  </svg>
  <div class="badge">
    <svg viewBox="0 0 24 24" fill="none" stroke="currentColor" stroke-width="2" stroke-linecap="round" stroke-linejoin="round"><rect x="3" y="3" width="18" height="13" rx="2"/><circle cx="9" cy="8" r="2"/><path d="M6 14c0-2 1.5-3 3-3s3 1 3 3M14 10h4M8 20h8M12 16v4"/></svg>
    ONLINE TRAINING
  </div>
  <p class="caption caption--training"><span class="caption__title">Pre-New Year’s Eve</span><span class="caption__sub">Dinsdag 29 December, 19-21u</span></p>
  <div class="brand"><span class="brand__name">Bright Path</span><span class="brand__tag">ACADEMY</span></div>
</section>

<!-- Podcast -->
<section class="post post--podcast">
  <svg class="post__art" viewBox="0 0 349 349">
    <polygon class="band" points="234,0 349,0 349,115 115,349 0,349 0,234"/>
    <circle class="ring" cx="175" cy="174" r="139"/>
    <g role="img" aria-label="Foto: podcastgast met gekruiste armen in een kantoor">
      <circle cx="175" cy="174" r="128" fill="url(#photoTone)"/>
      <circle cx="175" cy="174" r="128" fill="url(#photoShade)"/>
    </g>
  </svg>
  <div class="badge">
    <svg viewBox="0 0 24 24" fill="none" stroke="currentColor" stroke-width="2" stroke-linecap="round" stroke-linejoin="round"><rect x="9" y="3" width="6" height="11" rx="3"/><path d="M5 11a7 7 0 0 0 14 0M12 18v3"/></svg>
    PODCAST
  </div>
  <p class="caption caption--podcast"><span class="caption__lead">Kijk eens verder met</span><span class="caption__name">Joris van Daalen</span></p>
  <div class="brand"><span class="brand__name">Bright Path</span><span class="brand__tag">ACADEMY</span></div>
</section>

<!-- Facts -->
<section class="post post--facts">
  <svg class="post__art" viewBox="0 0 349 349">
    <polygon class="band" points="234,0 349,0 349,115 115,349 0,349 0,234"/>
    <circle class="ring" cx="175" cy="174" r="139"/>
    <g role="img" aria-label="Foto: vrouw met bril en tablet in een licht kantoor">
      <circle cx="175" cy="174" r="128" fill="url(#photoTone)"/>
      <circle cx="175" cy="174" r="128" fill="url(#photoShade)"/>
    </g>
  </svg>
  <div class="badge">
    <svg viewBox="0 0 24 24" fill="none" stroke="currentColor" stroke-width="2" stroke-linecap="round" stroke-linejoin="round"><path d="M4 10v4h4l5 4V6L8 10z"/><path d="M16 9a4 4 0 0 1 0 6M18.5 6.5a8 8 0 0 1 0 11"/></svg>
    FACTS
  </div>
  <p class="caption caption--facts">“Gemiddeld haalt slechts 20% zijn/haar goede voornemens”</p>
  <div class="brand"><span class="brand__name">Bright Path</span><span class="brand__tag">ACADEMY</span></div>
</section>
</body>
</html>
```